Briarvale Dental Care needs a functioning website with Wordpress

Our dental office needs a fully coded and functioning simple (3 page) website with Wordpress for us to be able to modify the content and add pages/tabs and be able to upload to Hostlark Linux hosting with cPanels for publication. The page should be professional, warm, inviting and easy to use and follow and content should be optimized for Google search engine visibility. Please see the current temporary site for details of the office including contact info and mission: www.briarvaledentalcare.ca also see the attached files for logo and office photos.

Target Market(s)

Families

Industry/Entity Type

Dental Clinic

Coding

Coded - Design and coding required

Number of Pages Required

3 page

Font styles to use
Sans Serif

Requirements
Must have
• Wordpress coding, contact info, mission, photos, keywords and content for Google search engine optimization, my logo, empty common tabs for us to be able to add content later such as services, hours, about us, etc.

```html
<!DOCTYPE html>
<html lang="en">
<head>
<meta charset="utf-8">
<title>Briarvale Dental Care</title>
<link rel="stylesheet" href="https://fonts.googleapis.com/css2?family=Noto+Serif:wght@400;700&family=PT+Sans:wght@400;700&display=swap">
<style>
:root{
  --green:#8cb42b;
  --ink:#222222;
  --text:#555555;
  --muted:#888888;
  --paper:#ffffff;
  --sand:#eeeee6;
  --footer-light:#ededE8;
  --footer-dark:#1c1c1c;
  --footer-darker:#141414;
  --line:#e2e2e2;
}
*{margin:0;padding:0;box-sizing:border-box}
html,body{width:1200px;height:2308px;overflow:hidden;background:var(--paper)}
body{font-family:"PT Sans",Arial,sans-serif;color:var(--text);position:relative}
.serif{font-family:"Noto Serif",Georgia,serif}

/* header */
.site-header{position:absolute;top:0;left:0;width:1200px;height:90px;background:#fff;border-top:2px solid #c9dc8e;border-bottom:1px solid var(--line)}
.brand{position:absolute;left:112px;top:20px;display:flex;align-items:center;gap:10px}
.brand-dot{width:34px;height:34px;border-radius:50%;background:var(--green)}
.brand-name{font-family:"Noto Serif",Georgia,serif;font-size:22px;line-height:22px;color:var(--green);text-transform:uppercase;width:170px}
.main-nav{position:absolute;right:110px;top:25px;display:flex;gap:0}
.main-nav a{display:block;font-family:"Noto Serif",Georgia,serif;font-size:12px;color:#444;text-decoration:none;padding:0 23px;height:40px;line-height:40px;text-transform:uppercase}
.main-nav a.active{border:1px solid var(--green);margin-right:22px;padding:0 17px}

/* hero */
.hero{position:absolute;top:90px;left:0;width:1200px;height:497px}
.hero-photo{position:absolute;inset:0;background:linear-gradient(90deg,#f3f3f3 0%,#eeeeee 40%,#dfe8ec 60%,#c6dbe3 75%,#c08c5c 95%,#b47a48 100%)}
.hero-copy{position:absolute;left:110px;top:248px;width:760px}
.hero-copy h1{font-family:"Noto Serif",Georgia,serif;font-weight:700;font-size:25px;line-height:31px;color:#1e1e1e;text-transform:uppercase}
.hero-copy p{margin-top:12px;font-size:11.5px;line-height:26px;color:#666;width:660px}
.hero-arrows{position:absolute;left:112px;top:415px;display:flex;gap:6px}
.hero-arrows span{width:19px;height:19px;border-radius:50%;background:#222;display:flex;align-items:center;justify-content:center}

/* section heads */
.section-title{font-family:"Noto Serif",Georgia,serif;font-weight:400;color:#1e1e1e;text-align:center;text-transform:uppercase}
.divider{display:block;margin:0 auto}

/* welcome */
.welcome{position:absolute;top:587px;left:0;width:1200px;height:286px;text-align:center}
.welcome h2{font-size:25px;margin-top:44px}
.welcome h3{font-family:"Noto Serif",Georgia,serif;font-weight:400;font-size:19px;color:#444;margin-top:14px;text-transform:uppercase}
.welcome .divider{margin-top:14px}
.welcome p{width:980px;margin:16px auto 0;font-size:11.5px;line-height:29px;color:#666}

/* services */
.services{position:absolute;top:873px;left:0;width:1200px;height:567px}
.services-photo{position:absolute;inset:0;background:linear-gradient(90deg,#b9b9b9 0%,#dedede 15%,#e8e8e8 50%,#d8d8d8 85%,#9c9c9c 100%)}
.services-panel{position:absolute;left:85px;top:67px;width:1028px;height:500px;background:rgba(246,246,246,0.93);box-shadow:0 0 8px rgba(0,0,0,0.12);text-align:center}
.services-panel h2{font-size:25px;margin-top:44px}
.services-panel .divider{margin-top:12px}
.services-panel > p{width:960px;margin:14px auto 0;font-size:11.5px;line-height:29px;color:#666}
.service-list{position:absolute;left:25px;top:200px;display:flex;gap:25px;text-align:left}
.service{width:226px}
.service-photo{width:226px;height:156px;border:4px solid #fff;box-shadow:0 0 3px rgba(0,0,0,0.25)}
.service h4{font-size:15px;font-weight:700;color:#222;margin-top:20px}
.service p{font-size:11px;line-height:25px;color:#666;margin-top:6px;text-align:justify}
.slide-arrow{position:absolute;top:366px;width:30px;height:42px;background:#fff;display:flex;align-items:center;justify-content:center;box-shadow:0 0 4px rgba(0,0,0,0.2)}
.slide-arrow.prev{left:58px;border-radius:21px 0 0 21px}
.slide-arrow.next{left:1113px;border-radius:0 21px 21px 0}

/* why choose */
.why{position:absolute;top:1440px;left:0;width:1200px;height:326px;background:var(--sand)}
.why-copy{position:absolute;left:110px;top:40px;width:500px}
.why-copy h2{font-family:"Noto Serif",Georgia,serif;font-weight:400;font-size:20px;color:#1e1e1e;text-transform:uppercase}
.why-copy > p{font-size:11.5px;line-height:25px;color:#999;margin-top:4px;padding-left:3px}
.why-list{list-style:none;margin-top:12px;padding-left:32px}
.why-list li{display:flex;align-items:center;gap:10px;font-size:12px;color:#333;height:41px}
.gallery{position:absolute;left:641px;top:43px;display:grid;grid-template-columns:repeat(3,138px);gap:20px 18px}
.gallery div{height:101px;border:3px solid #fff;box-shadow:0 0 4px rgba(0,0,0,0.25)}

/* testimonials */
.testimonials{position:absolute;top:1766px;left:0;width:1200px;height:324px;text-align:center}
.testimonials h2{font-size:25px;margin-top:44px}
.testimonials .divider{margin-top:12px}
.quote{position:absolute;top:138px;display:flex;gap:22px;text-align:left;width:480px}
.quote.one{left:110px}.quote.two{left:612px}
.avatar{flex:none;width:106px;height:106px;border-radius:50%;border:4px solid #fff;box-shadow:0 0 4px rgba(0,0,0,0.3)}
.quote blockquote{font-size:11px;line-height:26px;color:#666;margin-top:6px}
.quote cite{display:block;font-style:normal;font-weight:700;font-size:12px;color:var(--green);margin-top:6px}
.dots{position:absolute;top:274px;left:580px;display:flex;gap:4px}
.dots span{width:9px;height:9px;border-radius:50%;background:#ddd}
.dots span.on{background:#aaa}

/* footer */
.footer-links{position:absolute;top:2090px;left:0;width:1200px;height:76px;background:var(--footer-light);text-align:center;font-size:11.5px;color:#333;line-height:76px}
.footer-links a{color:#333;text-decoration:none;margin:0 8px}
.footer-contact{position:absolute;top:2166px;left:0;width:1200px;height:69px;background:var(--footer-dark);color:#eee;font-size:11.5px}
.contact-row{position:absolute;left:110px;top:0;height:69px;display:flex;align-items:center;gap:40px}
.contact-row span{display:flex;align-items:center;gap:9px}
.social{position:absolute;right:110px;top:22px;display:flex;gap:8px}
.social span{width:25px;height:25px;border-radius:50%;background:var(--green)}
.copyright{position:absolute;top:2235px;left:0;width:1200px;height:73px;background:var(--footer-darker);color:#888;font-size:11px;text-align:center;line-height:73px}
</style>
</head>
<body>

<header class="site-header">
  <div class="brand"><span class="brand-dot"></span><span class="brand-name">Briarvale Dental Care</span></div>
  <nav class="main-nav">
    <a class="active" href="#">Home</a>
    <a href="#">About Us</a>
    <a href="#">Services</a>
    <a href="#">Treatments</a>
    <a href="#">News</a>
    <a href="#">Contact</a>
  </nav>
</header>

<section class="hero">
  <div class="hero-photo" role="img" aria-label="Smiling patient giving a thumbs up in a dental chair"></div>
  <div class="hero-copy">
    <h1>Our goal is to provide you and your loved ones a comfortable dental experience.</h1>
    <p>Lorem ipsum dolor sit amet, consectetuer adipiscing elit, sed diam nonummy nibh euismod tincidunt ut laoreet dolore magna aliquam erat volutpat. Ut wisi enim ad minim veniam, quis nostrud exerci tation ullamcorper suscipit lobortis nisl ut aliquip ex ea commodo consequat.</p>
  </div>
  <div class="hero-arrows">
    <span><svg width="8" height="10" viewBox="0 0 8 10"><path d="M6 1L2 5l4 4" stroke="#fff" stroke-width="2" fill="none"/></svg></span>
    <span><svg width="8" height="10" viewBox="0 0 8 10"><path d="M2 1l4 4-4 4" stroke="#fff" stroke-width="2" fill="none"/></svg></span>
  </div>
</section>

<section class="welcome">
  <h2 class="section-title">Welcome to Briarvale Dental Care</h2>
  <h3>Family Dedicated Dental Practice</h3>
  <svg class="divider" width="90" height="12" viewBox="0 0 90 12"><rect x="0" y="5" width="34" height="2" fill="#8cb42b"/><rect x="56" y="5" width="34" height="2" fill="#8cb42b"/><rect x="40" y="1" width="10" height="10" rx="2" fill="#8cb42b"/></svg>
  <p>Etiam sagittis hendrerit ligula, sed condimentum dolor pellentesque vitae. Duis vel suscipit tellus. Nullam molestie, lorem at venenatis finibus, tellus metus bibendum arcu, ac eleifend metus magna sed diam. Curabitur eu tellus est. Curabitur vulputate diam metus, id aliquam orci accumsan non. Nam auctor nunc sapien, eget tincidunt sem tristique quis. Lorem ipsum dolor sit amet, consectetur adipiscing elit. Nullam pellentesque nibh nunc, in lobortis diam pellentesque quis. In sagittis eleifend posuere.</p>
</section>

<section class="services">
  <div class="services-photo" role="img" aria-label="Bright dental treatment room in soft focus"></div>
  <div class="services-panel">
    <h2 class="section-title">Our Services</h2>
    <svg class="divider" width="90" height="12" viewBox="0 0 90 12"><rect x="0" y="5" width="34" height="2" fill="#8cb42b"/><rect x="56" y="5" width="34" height="2" fill="#8cb42b"/><rect x="40" y="1" width="10" height="10" rx="2" fill="#8cb42b"/></svg>
    <p>Sed fringilla erat rutrum, facilisis ante at, consectetur mauris. Morbi ullamcorper, mi vel molestie dignissim, erat mi porta ipsum, eget lacinia ex quam quis metus. Cras ultrices sem tellus, vel iaculis sapien sollicitudin a. Vivamus rhoncus leo vel magna finibus pretium.</p>
    <div class="service-list">
      <article class="service">
        <div class="service-photo" role="img" aria-label="Dentist examining a young patient" style="background:linear-gradient(135deg,#7d8e96,#c9b9a8 60%,#8b6f5e)"></div>
        <h4>General Dentistry</h4>
        <p>Lorem ipsum dolor sit amet, consectetur adipiscing elit. Duis eget ex eget urna porttitor lobortis sed ut nulla.</p>
      </article>
      <article class="service">
        <div class="service-photo" role="img" aria-label="Dental assistant with a smiling child" style="background:linear-gradient(135deg,#d9d4cf,#b7b0a8 50%,#8e8a86)"></div>
        <h4>Children's Dentistry</h4>
        <p>Nullam sed mauris ornare, semper tellus nec, venenatis tellus. Etiam orci ligula, ullamcorper nec mauris vel, placerat sodales massa.</p>
      </article>
      <article class="service">
        <div class="service-photo" role="img" aria-label="Dentist talking with a senior patient" style="background:linear-gradient(135deg,#9fc1d6,#d8d4ce 50%,#5f9fc2)"></div>
        <h4>Senior's Dentistry</h4>
        <p>Aliquam ut rutrum justo. Vestibulum molestie eros id diam lacinia, non sagittis odio convallis. Aliquam sed magna consectetur.</p>
      </article>
      <article class="service">
        <div class="service-photo" role="img" aria-label="Smiling patient in a dental chair" style="background:linear-gradient(135deg,#e9e9e9,#c4b2a4 55%,#9cc43c)"></div>
        <h4>Cosmetic Dentistry</h4>
        <p>Donec facilisis lacus libero, sit amet euismod orci fringilla nec. Aenean sed metus ac sapien tempor aliquam eu eget massa.</p>
      </article>
    </div>
  </div>
  <span class="slide-arrow prev"><svg width="8" height="10" viewBox="0 0 8 10"><path d="M6 1L2 5l4 4" stroke="#333" stroke-width="1.5" fill="none"/></svg></span>
  <span class="slide-arrow next"><svg width="8" height="10" viewBox="0 0 8 10"><path d="M2 1l4 4-4 4" stroke="#333" stroke-width="1.5" fill="none"/></svg></span>
</section>

<section class="why">
  <div class="why-copy">
    <h2>Why choose Briarvale Dental Care</h2>
    <p>Ut wisi enim ad minim veniam, quis nostrud exerci tation ullamcorper suscipit lobortis nisl ut aliquip ex ea commodo consequat.</p>
    <ul class="why-list">
      <li><svg width="11" height="11" viewBox="0 0 11 11"><circle cx="5.5" cy="5.5" r="5.5" fill="#8cb42b"/><path d="M4.5 3l2.5 2.5-2.5 2.5" stroke="#fff" stroke-width="1.4" fill="none"/></svg>Nam liber tempor cum soluta nobis eleifend option congue</li>
      <li><svg width="11" height="11" viewBox="0 0 11 11"><circle cx="5.5" cy="5.5" r="5.5" fill="#8cb42b"/><path d="M4.5 3l2.5 2.5-2.5 2.5" stroke="#fff" stroke-width="1.4" fill="none"/></svg>Nihil imperdiet doming id quod mazim placerat facer possim assum</li>
      <li><svg width="11" height="11" viewBox="0 0 11 11"><circle cx="5.5" cy="5.5" r="5.5" fill="#8cb42b"/><path d="M4.5 3l2.5 2.5-2.5 2.5" stroke="#fff" stroke-width="1.4" fill="none"/></svg>Typi non habent claritatem insitam; est usus legentis in iis qui facit eorum claritatem</li>
      <li><svg width="11" height="11" viewBox="0 0 11 11"><circle cx="5.5" cy="5.5" r="5.5" fill="#8cb42b"/><path d="M4.5 3l2.5 2.5-2.5 2.5" stroke="#fff" stroke-width="1.4" fill="none"/></svg>Investigationes demonstraverunt lectores legere me lius quod ii legunt saepius.</li>
    </ul>
  </div>
  <div class="gallery">
    <div role="img" aria-label="Clinic entrance with front doors" style="background:linear-gradient(180deg,#c9c7b4,#6b6f7a 60%,#3b4256)"></div>
    <div role="img" aria-label="Waiting room with green chairs" style="background:linear-gradient(180deg,#6f6f6f,#4fb05a 60%,#606060)"></div>
    <div role="img" aria-label="Dental imaging equipment" style="background:linear-gradient(180deg,#6a6a6a,#cfcfcf 50%,#7a7a7a)"></div>
    <div role="img" aria-label="Clinic sign on a frosted wall" style="background:linear-gradient(135deg,#9a9a9a,#d8d8d8 50%,#8e8e8e)"></div>
    <div role="img" aria-label="Treatment room with green dental chair" style="background:linear-gradient(180deg,#8a8a8a,#d4d4d4 40%,#5fb56a 80%)"></div>
    <div role="img" aria-label="Sterilised instrument trays" style="background:linear-gradient(135deg,#5a5a5a,#e4e4e4 50%,#6cc14a)"></div>
  </div>
</section>

<section class="testimonials">
  <h2 class="section-title">Testimonials</h2>
  <svg class="divider" width="90" height="12" viewBox="0 0 90 12"><rect x="0" y="5" width="34" height="2" fill="#8cb42b"/><rect x="56" y="5" width="34" height="2" fill="#8cb42b"/><rect x="40" y="1" width="10" height="10" rx="2" fill="#8cb42b"/></svg>
  <div class="quote one">
    <div class="avatar" role="img" aria-label="Portrait of a patient" style="background:linear-gradient(135deg,#f2f2f2,#c7b7a6 60%,#6a6a6a)"></div>
    <div>
      <blockquote>&ldquo; Lorem ipsum dolor sit amet, consectetuer adipiscing elit, sed diam nonummy nibh euismod tincidunt ut laoreet &rdquo;</blockquote>
      <cite>- Clara Wynn</cite>
    </div>
  </div>
  <div class="quote two">
    <div class="avatar" role="img" aria-label="Portrait of a patient" style="background:linear-gradient(135deg,#c08c5c,#d9c4b2 50%,#bcd9e4)"></div>
    <div>
      <blockquote>&ldquo; Ut wisi enim ad minim veniam, quis nostrud exerci tation ullamcorper suscipit lobortis nisl ut aliquip &rdquo;</blockquote>
      <cite>- Clara Wynn</cite>
    </div>
  </div>
  <div class="dots"><span></span><span class="on"></span><span></span></div>
</section>

<nav class="footer-links">
  <a href="#">Home</a>|<a href="#">About Us</a>|<a href="#">Services</a>|<a href="#">FAQ</a>|<a href="#">Our Location</a>|<a href="#">Contact Us</a>|<a href="#">Privacy Statement</a>|<a href="#">News</a>|<a href="#">Site Terms</a>
</nav>

<footer class="footer-contact">
  <div class="contact-row">
    <span><svg width="9" height="13" viewBox="0 0 9 13"><path d="M4.5 0a4.5 4.5 0 0 0-4.5 4.5C0 8 4.5 13 4.5 13S9 8 9 4.5A4.5 4.5 0 0 0 4.5 0z" fill="#8cb42b"/><circle cx="4.5" cy="4.5" r="1.6" fill="#1c1c1c"/></svg>14-82 Linden Grove Road, Briarvale, ON K2B 4R7</span>
    <span><svg width="14" height="14" viewBox="0 0 14 14"><rect width="14" height="14" rx="3" fill="#8cb42b"/><path d="M4 3.5c0 4 2.5 6.5 6.5 6.5l.5-1.8-2-.8-.9.9C7 7.7 6.3 7 5.7 5.9l.9-.9-.8-2z" fill="#1c1c1c"/></svg>555-018-2247</span>
    <span><svg width="14" height="14" viewBox="0 0 14 14"><rect x="1" y="3" width="12" height="10" rx="1" fill="#8cb42b"/><rect x="3" y="0" width="6" height="4" fill="#8cb42b"/><rect x="3" y="6" width="8" height="1.5" fill="#1c1c1c"/><rect x="3" y="9" width="8" height="1.5" fill="#1c1c1c"/></svg>555-018-2247</span>
    <span><svg width="15" height="11" viewBox="0 0 15 11"><rect width="15" height="11" rx="1.5" fill="#8cb42b"/><path d="M1 1.5l6.5 5 6.5-5" stroke="#1c1c1c" stroke-width="1.3" fill="none"/></svg>reception@briarvaledentalcare.ca</span>
  </div>
  <div class="social"><span></span><span></span><span></span><span></span></div>
</footer>

<div class="copyright">2016 @ Briarvale Dental Care. All Right Reserved.</div>

</body>
</html>
```